Presentation Folder and Inserts for Scientific Recruiting Firm

Harborline Talent is a Pharmaceutical and Biotech recruiting firm. We help companies locate ideal candidates to fill positions within their companies. We want to have presentation materials designed to be handed out to clients at career fairs.

 

WE ARE OPEN TO ALL TYPES OF DESIGNS. 

 

We will have the need for the design of many more projects in the coming months.  We would love to find a great designer to work with on all of our future work.  

 

Part 1: Presentation Folder

A presentation folder designed to contain information about Harborline Talent and our company’s capabilities. This folder should be very professional and give the feeling that our company is reliable. Abstract designs are fine; incorporating different areas of science would be nice as well. We are open to colors/designs but the logo colors must not be changed.

We are looking for something simple and not too busy.  If you can incorporate the above that is great, but we are looking for a simple design.

 

Part 2: Folder Inserts

In one of the pockets of the folder we would like to have three sheets of paper. The paper will be displayed in a descending fashion so that you are able to see the 1.5 inch header on the top of each paper. (Full sheet in back, sheet trimmed 1.5 inches, sheet trimmed 3 inches in the front. The top 1.5 inch border is all that will need to be designed; we will trim the sheets after printing.

Target Market(s)

Human Resources professionals and hiring managers of biotech, pharmaceutical, and scientific companies

Requirements
Must have
• Folder:

• - Harborline Talent Logo Must been on white background
• - Company slogan must be on the cover, “Where Talent Meets Research”
• Interior
• - Must include space for a business card to be attached on one of the folder flaps
• - The logo and Slogan should also appear on one of the folder interior pocket flaps

• Please use the attached AI format from the company that will be printing out materials There is an outside and inside printing format.

•  

• Inserts:

• - Inserts must have Harborline Talent Logo on header
• - Insert must have design on the 1.5 inch of the page (Three Pages)
• - Three Sheets must be labeled, Direct Hire, Temporary Staffing, About Harborline Talent (This text layer must be left editable in the file delivered version for future revisions)

Nice to have
• Pictures or silhouettes of people
• Something incorporating different scientific themes

• Something incorporating several areas of science. Just a few ideas but there are countless areas of science, (Electronics, Medical, Environmental, Pharmaceutical, Biotech, Chemical, Aerospace, Engineering)
Should not have
• We are open to anything that you can think of.  We want to base an entire series of promotional materials on these designs so we are open minded.

```html
<!DOCTYPE html>
<html lang="en">
<head>
<meta charset="utf-8">
<title>Harborline Talent – Presentation Folder</title>
<link rel="stylesheet" href="https://fonts.googleapis.com/css2?family=Barlow:wght@400;500;600&family=Tinos&display=swap">
<style>
  :root{
    --green:#1f6b33;
    --green-deep:#17562a;
    --green-faint:#2a7a3e;
    --olive:#6b6a2a;
    --gold:#c98a1e;
    --paper:#ffffff;
    --grid:#eef0ee;
    --grey-light:#e6e6e6;
    --grey-mid:#c9c9c9;
    --ink:#333333;
  }
  *{box-sizing:border-box;margin:0;padding:0}
  html,body{width:1200px;height:2492px;overflow:hidden;background:#fff}
  .canvas{position:relative;width:1200px;height:2492px;overflow:hidden;background:#fff;font-family:"Barlow",sans-serif}

  /* photo tiles */
  .tile-row{display:flex;width:100%}
  .tile{position:relative;flex:1 1 0;height:100%}
  .tile-label{position:absolute;left:0;right:0;bottom:6px;text-align:center;color:#fff;font-size:9px;font-weight:500;letter-spacing:1.4px;text-transform:uppercase}

  .logo-band{position:relative;background-color:var(--paper);
    background-image:linear-gradient(var(--grid) 1px,transparent 1px),linear-gradient(90deg,var(--grid) 1px,transparent 1px);
    background-size:14px 14px}
  .brand-name{font-family:"Barlow",sans-serif;font-weight:500;color:var(--green);letter-spacing:1px;text-transform:uppercase;white-space:nowrap}
  .brand-slogan{font-family:"Barlow",sans-serif;font-weight:600;color:var(--green);letter-spacing:1.5px;text-transform:uppercase;white-space:nowrap}

  /* flat front cover */
  .cover{position:absolute;left:322px;top:30px;width:555px;height:746px;display:flex;flex-direction:column;box-shadow:0 0 0 1px #ddd}
  .cover .tile-row{height:153px}
  .cover .logo-band{height:140px;display:flex;flex-direction:column;align-items:center;justify-content:center;gap:8px}
  .cover .brand-name{font-size:42px}
  .cover .brand-slogan{font-size:15px}

  /* outside spread */
  .outside{position:absolute;left:50px;top:853px;width:1109px;height:746px;display:flex;flex-direction:column;box-shadow:0 0 0 1px #ddd}
  .outside .tile-row{height:152px}
  .outside .logo-band{height:144px;display:flex}
  .outside .band-half{flex:1;position:relative;display:flex;flex-direction:column;align-items:center;justify-content:center;gap:8px}
  .outside .band-half + .band-half{border-left:1px solid #e0e0e0}
  .web-address{position:absolute;bottom:18px;left:0;right:0;text-align:center;font-size:17px;font-weight:600;color:var(--green);letter-spacing:1.5px}
  .outside .brand-name{font-size:40px}
  .outside .brand-slogan{font-size:14px}

  /* inside spread */
  .inside{position:absolute;left:46px;top:1698px;width:1121px;height:766px;overflow:hidden;background:var(--grey-light)}
  .inside-collage{position:absolute;inset:0;background:linear-gradient(135deg,#eeeeee 0%,#d4d4d4 35%,#e8e8e8 60%,#cfcfcf 100%)}
  .fold-line{position:absolute;left:563px;top:0;bottom:0;border-left:1px dashed #bbb}
  .inside-web{position:absolute;left:140px;top:226px;font-size:15px;font-weight:600;color:var(--green);letter-spacing:.5px}

  .insert{position:absolute;left:582px;top:37px;width:539px;height:520px;background:var(--paper)}
  .insert-tab{position:relative;overflow:hidden;display:flex;align-items:center;padding-left:28px;color:#fff;font-size:19px;font-weight:500;letter-spacing:1.5px;text-transform:uppercase}
  .insert-tab .ghost{position:absolute;left:12px;top:-14px;font-size:86px;font-weight:600;letter-spacing:2px;opacity:.12;white-space:nowrap}
  .insert-tab .tab-brand{position:absolute;right:14px;top:10px;font-size:13px;font-weight:500;letter-spacing:.8px;color:#fff;text-transform:uppercase}
  .tab-direct{height:96px;background:var(--green);align-items:flex-end;padding-bottom:24px}
  .tab-temp{height:78px;background:var(--olive)}
  .tab-about{height:111px;background:var(--gold)}
  .insert-body{padding:16px 30px 0 28px;font-family:"Tinos",serif;font-size:11.5px;line-height:1.4;color:var(--ink)}
  .insert-body p{margin-bottom:9px}

  .pocket{position:absolute;left:0;top:535px;width:1121px;height:231px}
  .card{position:absolute;top:34px;width:167px;height:142px;background:#fff;border-radius:14px;overflow:hidden}
  .card-left{left:129px}
  .card-right{left:683px}
  .card-head{height:44px;background:#dcdcdc;display:flex;align-items:center;justify-content:center}
  .card-head .brand-name{font-size:15px;letter-spacing:.5px}
  .card-body{padding:6px 12px;font-size:8px;line-height:1.35;color:var(--ink)}
  .card-name{color:var(--green);font-weight:600}
  .card-email{color:var(--gold)}
  .card-address{margin-top:8px}
</style>
</head>
<body>
<div class="canvas">

  <!-- front cover -->
  <section class="cover">
    <div class="tile-row">
      <div class="tile" style="flex:1.3;background:linear-gradient(135deg,#6d9a2c,#2f6a1c)" role="img" aria-label="Photo of a circuit board"><span class="tile-label">Electronics</span></div>
      <div class="tile" style="background:linear-gradient(180deg,#2f72b8,#b9d3ea)" role="img" aria-label="Photo of the earth from space"><span class="tile-label">Planetary</span></div>
    </div>
    <div class="tile-row">
      <div class="tile" style="background:linear-gradient(135deg,#c9d44a,#6e8d1e)" role="img" aria-label="Photo of liquid in a beaker"><span class="tile-label">Biotechnology</span></div>
      <div class="tile" style="flex:1.3;background:linear-gradient(180deg,#9cc3e4,#5d8f3e)" role="img" aria-label="Photo of wind turbines on a hill"><span class="tile-label">Wind Energy</span></div>
      <div class="tile" style="flex:.6;background:radial-gradient(circle,#7ed14a,#1f5a12)" role="img" aria-label="Micrograph of green cells"></div>
    </div>
    <div class="logo-band">
      <span class="brand-name">Harborline Talent</span>
      <span class="brand-slogan">Where Talent Meets Research</span>
    </div>
    <div class="tile-row">
      <div class="tile" style="background:linear-gradient(135deg,#8ab43a,#2c2c2c)" role="img" aria-label="Photo of a microscope lens"><span class="tile-label">Pharmaceutical</span></div>
      <div class="tile" style="background:linear-gradient(135deg,#2b5f95,#d9dde2)" role="img" aria-label="Photo of an aircraft wing"><span class="tile-label">Aerospace</span></div>
    </div>
    <div class="tile-row">
      <div class="tile" style="background:linear-gradient(135deg,#e4e8e6,#8aa0a2)" role="img" aria-label="Photo of a researcher writing in a lab"><span class="tile-label">Data Collection</span></div>
      <div class="tile" style="background:linear-gradient(135deg,#3b2a1a,#d2862c)" role="img" aria-label="Photo of light trails radiating outward"><span class="tile-label">New Energy Research</span></div>
      <div class="tile" style="flex:.5;background:linear-gradient(180deg,#a0202a,#5a0f14)" role="img" aria-label="Close-up photo of red texture"></div>
    </div>
  </section>

  <!-- outside spread -->
  <section class="outside">
    <div class="tile-row">
      <div class="tile" style="background:linear-gradient(180deg,#4f8a46,#a7d2d8)" role="img" aria-label="Photo of test tubes"><span class="tile-label">Biochemistry</span></div>
      <div class="tile" style="background:linear-gradient(135deg,#7b6a5a,#c7c9cc)" role="img" aria-label="Photo of a lab scientist holding a sample"><span class="tile-label">Pharmaceutical Research</span></div>
      <div class="tile" style="background:linear-gradient(135deg,#5f6670,#c4c8cc)" role="img" aria-label="Photo of a molecular structure model"><span class="tile-label">Chemical Compounds</span></div>
      <div class="tile" style="background:linear-gradient(135deg,#6d9a2c,#2f6a1c)" role="img" aria-label="Photo of a circuit board"><span class="tile-label">Electronics</span></div>
      <div class="tile" style="background:linear-gradient(180deg,#2f72b8,#b9d3ea)" role="img" aria-label="Photo of the earth from space"><span class="tile-label">Planetary</span></div>
    </div>
    <div class="tile-row">
      <div class="tile" style="flex:.55;background:linear-gradient(135deg,#5fb7b4,#0f3e48)" role="img" aria-label="Abstract teal liquid photo"></div>
      <div class="tile" style="flex:1;background:linear-gradient(135deg,#8fc23a,#2d5a14)" role="img" aria-label="Photo of gears"><span class="tile-label">Industrial Engineering</span></div>
      <div class="tile" style="flex:.85;background:linear-gradient(135deg,#1c3f8a,#d0803a)" role="img" aria-label="Photo of a space station interior"><span class="tile-label">Space Studies</span></div>
      <div class="tile" style="flex:1;background:linear-gradient(135deg,#c9d44a,#6e8d1e)" role="img" aria-label="Photo of liquid in a beaker"><span class="tile-label">Biotechnology</span></div>
      <div class="tile" style="flex:1.15;background:linear-gradient(180deg,#9cc3e4,#5d8f3e)" role="img" aria-label="Photo of wind turbines on a hill"><span class="tile-label">Wind Energy</span></div>
      <div class="tile" style="flex:.55;background:radial-gradient(circle,#7ed14a,#1f5a12)" role="img" aria-label="Micrograph of green cells"></div>
    </div>
    <div class="logo-band">
      <div class="band-half"><span class="web-address">HARBORLINETALENT.NET</span></div>
      <div class="band-half">
        <span class="brand-name">Harborline Talent</span>
        <span class="brand-slogan">Where Talent Meets Research</span>
      </div>
    </div>
    <div class="tile-row">
      <div class="tile" style="background:radial-gradient(circle,#f06aa0,#3a1f6a)" role="img" aria-label="Photo of a plasma globe"><span class="tile-label">Atomic Research</span></div>
      <div class="tile" style="background:linear-gradient(135deg,#1b3b70,#7ea3c8)" role="img" aria-label="Photo of solar panels"><span class="tile-label">Solar Power</span></div>
      <div class="tile" style="background:linear-gradient(135deg,#2f8a8e,#b6d7d2)" role="img" aria-label="Photo of machined metal parts"><span class="tile-label">Mechanical Engineering</span></div>
      <div class="tile" style="flex:.8;background:linear-gradient(135deg,#8ab43a,#3a3a2a)" role="img" aria-label="Photo of lab glassware"></div>
      <div class="tile" style="background:linear-gradient(135deg,#b0b5b8,#2a2a2a)" role="img" aria-label="Photo of a microscope lens"><span class="tile-label">Pharmaceutical</span></div>
      <div class="tile" style="background:linear-gradient(135deg,#2b5f95,#d9dde2)" role="img" aria-label="Photo of an aircraft wing"><span class="tile-label">Aerospace</span></div>
    </div>
    <div class="tile-row">
      <div class="tile" style="flex:.55;background:linear-gradient(135deg,#3a8a3a,#123a18)" role="img" aria-label="Photo of a green circuit board"></div>
      <div class="tile" style="background:linear-gradient(135deg,#6a5a3a,#c6b59a)" role="img" aria-label="Photo of a rocket engine"><span class="tile-label">Rocket Engineering</span></div>
      <div class="tile" style="background:linear-gradient(135deg,#2aa6a0,#cfeee8)" role="img" aria-label="Photo of glass vials"><span class="tile-label">Chemistry</span></div>
      <div class="tile" style="background:linear-gradient(135deg,#e4e8e6,#8aa0a2)" role="img" aria-label="Photo of a researcher writing in a lab"><span class="tile-label">Data Collection</span></div>
      <div class="tile" style="background:linear-gradient(135deg,#3b2a1a,#d2862c)" role="img" aria-label="Photo of light trails radiating outward"><span class="tile-label">New Energy Research</span></div>
      <div class="tile" style="flex:.45;background:linear-gradient(180deg,#a0202a,#5a0f14)" role="img" aria-label="Close-up photo of red texture"></div>
    </div>
  </section>

  <!-- inside spread -->
  <section class="inside">
    <div class="inside-collage" role="img" aria-label="Faded grey collage of science photos: lab work, aircraft, plasma and equipment"></div>
    <div class="fold-line"></div>
    <span class="inside-web">www.harborlinetalent.net</span>

    <div class="insert">
      <div class="insert-tab tab-direct"><span class="ghost">DIRECT</span>Direct Hire<span class="tab-brand">Harborline Talent</span></div>
      <div class="insert-tab tab-temp"><span class="ghost">TEMPORARY</span>Temporary Staffing<span class="tab-brand">Harborline Talent</span></div>
      <div class="insert-tab tab-about"><span class="ghost">ABOUT</span>About Harborline Talent<span class="tab-brand">Harborline Talent</span></div>
      <div class="insert-body">
        <p>Harborline Talent connects research organizations with scientists, engineers and technical specialists. Our recruiters understand the laboratory, the clinic and the production floor, so every introduction starts with a real fit.</p>
        <p>We work across pharmaceutical, biotech, chemical and engineering fields, supporting teams from early discovery through manufacturing and quality.</p>
        <p>Every search is handled by a consultant with a science background. We screen for technical depth, communication and culture, then present a short list of candidates ready to contribute from day one. Clients receive clear timelines and regular updates throughout.</p>
        <p>Partner with us for your next hire and see the difference focus makes.</p>
      </div>
    </div>

    <div class="pocket">
      <svg width="1121" height="231" viewBox="0 0 1121 231" aria-hidden="true">
        <defs>
          <clipPath id="pocket-shape">
            <polygon points="0,0 517,0 560,231 0,231"/>
            <polygon points="610,0 1121,0 1121,231 570,231"/>
          </clipPath>
        </defs>
        <g clip-path="url(#pocket-shape)">
          <rect width="1121" height="231" fill="#1f6b33"/>
          <text x="-20" y="52" font-family="Barlow, sans-serif" font-weight="600" font-size="62" fill="#2a7a3e" letter-spacing="3">HEMISTRY BIOTECHNOLOGY ELECTRONICS</text>
          <text x="10" y="92" font-family="Barlow, sans-serif" font-weight="600" font-size="30" fill="#2a7a3e" letter-spacing="3">ACE CHEMISTRY TECHNOLOGY ENGINEERING PHARMACEUTICAL ELECTRONICS</text>
        </g>
      </svg>
      <div class="card card-left">
        <div class="card-head"><span class="brand-name">Harborline Talent</span></div>
        <div class="card-body">
          <div><span class="card-name">Dana Reyes</span> <span class="card-email">dana@harborlinetalent.net</span></div>
          <div>1.503.555.0148</div>
          <div class="card-address">418 Quay Street<br>Portland, OR 97209</div>
        </div>
      </div>
      <div class="card card-right">
        <div class="card-head"><span class="brand-name">Harborline Talent</span></div>
        <div class="card-body">
          <div><span class="card-name">Dana Reyes</span> <span class="card-email">dana@harborlinetalent.net</span></div>
          <div>1.503.555.0148</div>
          <div class="card-address">418 Quay Street<br>Portland, OR 97209</div>
        </div>
      </div>
    </div>
  </section>

</div>
</body>
</html>
```